Korumel Business Card

We want a logo that connects with the target consumer who are Retailers in the giftware/wholesale/ecommerce space. We will be constantly changing product lines and industry. We are after a logo that can communicate the meaning of "Korumel"which means Divine/spiritual/light. The company name and owners are of Indian nationals and want to bring the positivity/growth in the design as a subtle message.
Have attached a logo that we think captures the essence of the word "Korumel" which is light/glow/divine.

Target Market(s)

Adults based in Australia english speaking aged 20 - 60 years that are in the retail business.

Industry/Entity Type

Business

Font styles to use
Serif
Sans Serif
Decorative
Script

Requirements
Must have
• Logo in form of "D" or "Korumel" or "Korumel Pty Ltd"
Nice to have
• I have attached a sample of letter D used as logo. Its shows the glowing sun which is representative/symbolic presentation of word "Korumel"

```html
<!DOCTYPE html>
<html lang="en">
<head>
<meta charset="utf-8">
<title>Korumel Business Card</title>
<link rel="stylesheet" href="https://fonts.googleapis.com/css2?family=Delius&family=Josefin+Slab:wght@400;600&display=swap">
<style>
  :root {
    --plum: #7d0a4f;
    --sun: #ffe400;
    --backdrop: #efe9e2;
    --shadow: rgba(60, 30, 10, 0.28);
  }
  * { box-sizing: border-box; margin: 0; padding: 0; }
  html, body { width: 1200px; height: 1000px; overflow: hidden; }
  body {
    background: var(--backdrop);
    position: relative;
    font-family: "Delius", "Comic Neue", sans-serif;
  }
  .card {
    position: absolute;
    width: 620px;
    height: 360px;
    box-shadow: 0 10px 24px var(--shadow);
    overflow: hidden;
  }
  /* Front */
  .card--front { left: 110px; top: 90px; display: flex; }
  .front__field {
    width: 400px;
    background: var(--plum);
    display: flex;
    align-items: center;
    padding-left: 95px;
  }
  .front__wordmark {
    font-family: "Josefin Slab", serif;
    font-weight: 600;
    font-size: 56px;
    letter-spacing: 10px;
    color: var(--sun);
  }
  .front__mark {
    flex: 1;
    background: var(--sun);
    display: flex;
    align-items: center;
    justify-content: center;
    gap: 12px;
  }
  .brand-dot {
    width: 22px; height: 22px; border-radius: 50%;
    background: var(--plum);
    flex: none;
  }
  .brand-name {
    font-size: 34px;
    color: var(--plum);
  }
  /* Back */
  .card--back {
    left: 470px; top: 550px;
    background: var(--sun);
    color: var(--plum);
  }
  .back__mark {
    position: absolute;
    left: 36px; top: 150px;
    display: flex; align-items: center; gap: 10px;
  }
  .back__mark .brand-name { font-size: 30px; }
  .back__details {
    position: absolute;
    left: 345px; top: 52px;
  }
  .holder__name { font-size: 22px; letter-spacing: 1px; }
  .holder__role { font-size: 14px; margin-top: 2px; }
  .holder__location { font-size: 18px; margin-top: 42px; }
  .contact { list-style: none; margin-top: 60px; font-size: 18px; line-height: 1.45; }
  .contact li { display: flex; align-items: center; gap: 12px; }
  .contact svg { width: 20px; height: 20px; flex: none; }
</style>
</head>
<body>
  <section class="card card--front">
    <div class="front__field">
      <span class="front__wordmark">Korumel</span>
    </div>
    <div class="front__mark">
      <span class="brand-dot"></span>
      <span class="brand-name">Korumel</span>
    </div>
  </section>

  <section class="card card--back">
    <div class="back__mark">
      <span class="brand-dot"></span>
      <span class="brand-name">Korumel</span>
    </div>
    <div class="back__details">
      <p class="holder__name">Korumel</p>
      <p class="holder__role">Managing Director</p>
      <p class="holder__location">Ann St Brisbane - Australia</p>
      <ul class="contact">
        <li>
          <svg viewBox="0 0 20 20" aria-hidden="true"><rect x="5" y="1.5" width="10" height="17" rx="2" fill="none" stroke="currentColor" stroke-width="1.6"/><circle cx="10" cy="15.5" r="1" fill="currentColor"/></svg>
          <span>+61 400 123 456</span>
        </li>
        <li>
          <svg viewBox="0 0 20 20" aria-hidden="true"><path d="M3 7c0-2 3-3 7-3s7 1 7 3v2h-4V7.5H7V9H3z" fill="currentColor"/><rect x="4" y="10" width="12" height="7" rx="2" fill="none" stroke="currentColor" stroke-width="1.6"/></svg>
          <span>+61 7 3100 2200</span>
        </li>
        <li>
          <svg viewBox="0 0 20 20" aria-hidden="true"><rect x="2" y="5" width="16" height="11" fill="currentColor"/><path d="M2 5l8 6 8-6" fill="none" stroke="#ffe400" stroke-width="1.4"/></svg>
          <span>hello@korumel.com</span>
        </li>
      </ul>
    </div>
  </section>
</body>
</html>
```